Marnie's Hideaway Flyer

Need an attractive flyer for an existing Spa in SG around the Larkview area ( Former Meadow Hall) . Our spa is s converted horse stables , environment totally back to nature - see horse riding etc...even though it is located in the suburbs
Main business come from facials, waxing/hair removals, instant spraytan and body works. Flyer needs to attract new clients to our business.
Updates

I have done some updates on my requirements.

Target Market(s)

Adults of 25 -65 ( male and female), English speaking

Industry/Entity Type

Environment

Font styles to use
Script

Requirements
Must have
• Must have the 5 logos of the top brand products we use in the Spa.
Should not have
• No tacky designs. Must maintain class and decorum .
No animations too.

```html
<!DOCTYPE html>
<html lang="en">
<head>
<meta charset="utf-8">
<title>Marnie's Hideaway Flyer</title>
<link href="https://fonts.googleapis.com/css2?family=Cormorant+Garamond:wght@500&family=Open+Sans:wght@400;600&family=Parisienne&display=swap" rel="stylesheet">
<style>
  :root {
    --page: #ecebe8;
    --paper: #ffffff;
    --stone: #cfcfcf;
    --ruby: #c0202e;
    --ruby-dark: #9e1622;
    --ink: #3a3a3a;
    --ink-soft: #555555;
    --script: #8a8a8a;
  }
  * { box-sizing: border-box; margin: 0; padding: 0; }
  html, body { width: 1200px; height: 883px; overflow: hidden; }
  body { background: var(--page); font-family: "Open Sans", Arial, sans-serif; position: relative; }

  .flyer { position: absolute; background: var(--paper); overflow: hidden; box-shadow: 0 2px 8px rgba(0,0,0,.18); }
  .flyer--front { left: 37px; top: 24px; width: 549px; height: 777px; }
  .flyer--back { left: 612px; top: 53px; width: 551px; height: 780px; }
  .flyer__art { position: absolute; inset: 0; width: 100%; height: 100%; }

  .brand-name { position: absolute; font-family: "Cormorant Garamond", Georgia, serif; font-weight: 500; color: var(--ink); font-size: 36px; line-height: 1; white-space: nowrap; }
  .flyer--front .brand-name { left: 0; right: 0; top: 50px; text-align: center; }
  .flyer--back .brand-name { left: 33px; top: 96px; }

  .headline { position: absolute; left: 30px; right: 30px; top: 111px; text-align: center; color: var(--ruby); font-size: 19px; line-height: 25px; letter-spacing: .2px; }

  .tagline { position: absolute; font-family: "Parisienne", cursive; color: var(--script); font-size: 21px; line-height: 31px; }
  .flyer--front .tagline { left: 326px; width: 210px; top: 297px; text-align: center; }
  .flyer--back .tagline { right: 22px; top: 32px; font-size: 22px; }

  .lead { position: absolute; left: 0; right: 0; top: 605px; text-align: center; color: var(--paper); font-size: 17px; line-height: 27px; }

  .phone { position: absolute; left: 0; right: 0; top: 670px; text-align: center; color: var(--ruby); font-size: 24px; line-height: 34px; display: flex; justify-content: center; align-items: center; gap: 10px; }
  .phone svg { width: 26px; height: 22px; }

  .outlets { position: absolute; left: 0; right: 0; text-align: center; color: var(--ink); font-size: 14px; }
  .flyer--front .outlets { top: 719px; }
  .flyer--back .outlets { top: 680px; }

  .intro { position: absolute; left: 29px; right: 30px; top: 170px; color: var(--ink-soft); font-size: 13.5px; line-height: 21px; }

  .services { position: absolute; left: 0; right: 0; top: 246px; display: flex; justify-content: center; align-items: center; gap: 14px; color: var(--ruby); font-size: 21px; list-style: none; }
  .services .dash { width: 3px; height: 9px; background: var(--script); transform: skewX(-20deg); border-radius: 1px; }

  .hours { position: absolute; left: 0; right: 0; top: 549px; text-align: center; color: var(--paper); font-size: 14px; line-height: 25px; }

  .web { position: absolute; left: 0; right: 0; top: 622px; display: flex; justify-content: center; align-items: center; gap: 10px; color: var(--ruby); font-size: 20px; font-weight: 600; }
  .web svg { width: 22px; height: 22px; }

  .partners { position: absolute; left: 0; right: 0; bottom: 0; height: 58px; background: var(--paper); display: flex; justify-content: space-around; align-items: center; padding: 0 18px; }
  .partner-badge { width: 82px; height: 22px; border-radius: 3px; }
  .partner-badge--teal { background: #2e8d8f; }
  .partner-badge--slate { background: #4a4a4a; }
  .partner-badge--rose { background: #c4404e; }
  .partner-badge--grey { background: #7a7a7a; }
  .partner-badge--dark { background: #2f2f2f; }
</style>
</head>
<body>

<section class="flyer flyer--front">
  <svg class="flyer__art" viewBox="0 0 418 591" preserveAspectRatio="none">
    <defs>
      <linearGradient id="frontPaper" x1="0" y1="0" x2="0" y2="1">
        <stop offset="0" stop-color="#ffffff"/>
        <stop offset=".6" stop-color="#f7f7f7"/>
        <stop offset="1" stop-color="#e6e6e6"/>
      </linearGradient>
      <radialGradient id="portraitTone" cx=".3" cy=".55" r=".75">
        <stop offset="0" stop-color="#e4bb9d"/>
        <stop offset=".45" stop-color="#edd0bb"/>
        <stop offset=".8" stop-color="#f7ebe2"/>
        <stop offset="1" stop-color="#ffffff" stop-opacity="0"/>
      </radialGradient>
      <linearGradient id="frontStone" x1="0" y1="0" x2="0" y2="1">
        <stop offset="0" stop-color="#d8d8d8"/>
        <stop offset="1" stop-color="#c4c4c4"/>
      </linearGradient>
      <radialGradient id="maskTone" cx=".5" cy=".45" r=".6">
        <stop offset="0" stop-color="#f7f1ea"/>
        <stop offset="1" stop-color="#d8c2b0"/>
      </radialGradient>
    </defs>
    <rect width="418" height="591" fill="url(#frontPaper)"/>
    <g role="img" aria-label="Photo of a smiling woman with bare shoulders">
      <rect x="0" y="170" width="330" height="250" fill="url(#portraitTone)"/>
    </g>
    <path d="M0,176 C60,146 130,140 200,145 C250,148 290,143 317,137 C280,155 230,165 180,167 C110,171 50,190 0,228 Z" fill="#000" opacity=".08"/>
    <path d="M0,170 C60,140 130,135 200,140 C250,143 290,138 317,132 C280,150 230,160 180,162 C110,166 50,185 0,222 Z" fill="var(--ruby)"/>
    <path d="M0,418 C90,396 180,404 260,412 C330,418 390,405 418,392 L418,591 L0,591 Z" fill="url(#frontStone)"/>
    <path d="M0,405 C80,385 170,395 260,405 C330,412 390,400 418,385 L418,400 C380,418 320,428 250,425 C170,420 80,412 0,432 Z" fill="var(--ruby)"/>
    <circle cx="345" cy="354" r="61" fill="var(--ruby)"/>
    <circle cx="345" cy="354" r="58" fill="#ffffff"/>
    <g role="img" aria-label="Photo of a woman relaxing with a facial mask and towel">
      <circle cx="345" cy="354" r="54" fill="url(#maskTone)"/>
    </g>
  </svg>

  <h1 class="brand-name">marnie's hideaway</h1>
  <p class="headline">LOOKING AND FEELING GOOD DOESN'T NEED<br>TO BE YOUR LITTLE SECRET.</p>
  <p class="tagline">The One-stop Salon<br>Spa of Choice</p>
  <p class="lead">From facials, Brazilian waxing to nails and body,<br>Marnie's Hideaway will always make you feel pampered...</p>
  <p class="phone">
    <svg viewBox="0 0 26 22" aria-hidden="true"><path d="M2,8 C2,3 24,3 24,8 L24,10 L18,10 L18,7 L8,7 L8,10 L2,10 Z M6,11 L20,11 L23,20 L3,20 Z" fill="var(--ruby)"/><circle cx="13" cy="15" r="3" fill="#ffffff"/></svg>
    6178 2904
  </p>
  <p class="outlets">Outlets: 100 Meadow Hall Road, #01-02c Stablegate</p>
</section>

<section class="flyer flyer--back">
  <svg class="flyer__art" viewBox="0 0 419 592" preserveAspectRatio="none">
    <defs>
      <linearGradient id="backPaper" x1="0" y1="0" x2="0" y2="1">
        <stop offset="0" stop-color="#ffffff"/>
        <stop offset="1" stop-color="#ededed"/>
      </linearGradient>
      <linearGradient id="backStone" x1="0" y1="0" x2="0" y2="1">
        <stop offset="0" stop-color="#dcdcdc"/>
        <stop offset="1" stop-color="#c4c4c4"/>
      </linearGradient>
      <radialGradient id="massageTone" cx=".5" cy=".5" r=".6"><stop offset="0" stop-color="#f0cfb6"/><stop offset="1" stop-color="#c99574"/></radialGradient>
      <radialGradient id="armTone" cx=".5" cy=".5" r=".6"><stop offset="0" stop-color="#f6e8de"/><stop offset="1" stop-color="#dcb79e"/></radialGradient>
      <radialGradient id="nailTone" cx=".5" cy=".5" r=".6"><stop offset="0" stop-color="#f3dccc"/><stop offset="1" stop-color="#d0a084"/></radialGradient>
    </defs>
    <rect width="419" height="592" fill="url(#backPaper)"/>
    <path d="M0,318 C80,288 150,284 220,289 C300,294 360,272 419,250 L419,548 L0,548 Z" fill="url(#backStone)"/>
    <path d="M0,300 C60,270 120,262 200,268 C280,274 350,252 419,232 L419,248 C360,268 300,284 220,282 C140,280 70,290 0,332 Z" fill="var(--ruby)"/>
    <circle cx="74" cy="325" r="56" fill="var(--ruby)"/>
    <circle cx="74" cy="325" r="53" fill="#ffffff"/>
    <g role="img" aria-label="Photo of a relaxing back massage"><circle cx="74" cy="325" r="49" fill="url(#massageTone)"/></g>
    <circle cx="209" cy="325" r="56" fill="var(--ruby)"/>
    <circle cx="209" cy="325" r="53" fill="#ffffff"/>
    <g role="img" aria-label="Photo of a smooth underarm after waxing"><circle cx="209" cy="325" r="49" fill="url(#armTone)"/></g>
    <circle cx="345" cy="325" r="56" fill="var(--ruby)"/>
    <circle cx="345" cy="325" r="53" fill="#ffffff"/>
    <g role="img" aria-label="Photo of manicured hands with a daisy"><circle cx="345" cy="325" r="49" fill="url(#nailTone)"/></g>
  </svg>

  <p class="tagline">The One-stop Salon / Spa of Choice</p>
  <h2 class="brand-name">marnie's hideaway</h2>
  <p class="intro">Marnie's Hideaway prides herself as " The One-stop Salon/Spa of Choice " catering for all your needs from top to toe.</p>
  <ul class="services">
    <li class="dash" aria-hidden="true"></li><li>Waxing</li>
    <li class="dash" aria-hidden="true"></li><li>Nails</li>
    <li class="dash" aria-hidden="true"></li><li>Spraytan</li>
    <li class="dash" aria-hidden="true"></li><li>Face</li>
    <li class="dash" aria-hidden="true"></li><li>Body</li>
    <li class="dash" aria-hidden="true"></li>
  </ul>
  <p class="hours">We are open daily.<br>Call in for special deals at the spa, or visit our website at:</p>
  <p class="web">
    <svg viewBox="0 0 22 22" aria-hidden="true"><circle cx="11" cy="11" r="8.5" fill="none" stroke="var(--ruby)" stroke-width="2.5"/><path d="M3,11 H19 M11,2.5 C7,7 7,15 11,19.5 M11,2.5 C15,7 15,15 11,19.5" fill="none" stroke="var(--ruby)" stroke-width="1.5"/></svg>
    www.marnieshideaway.sg
  </p>
  <p class="outlets">Outlets: 100 Meadow Hall Road, #01-02c Stablegate</p>
  <div class="partners" aria-label="Partner product brands">
    <span class="partner-badge partner-badge--teal"></span>
    <span class="partner-badge partner-badge--slate"></span>
    <span class="partner-badge partner-badge--rose"></span>
    <span class="partner-badge partner-badge--grey"></span>
    <span class="partner-badge partner-badge--dark"></span>
  </div>
</section>

</body>
</html>
```